lanternox munchies snack packaging

We are a new startup snack company that need a design for a snack packaging. Our snack goes by the name of lanternox munchies. Its a traditional snack usually eaten during festive seasons in south east asia region. The idea is to revolutionize the notion of the snack from one that is eaten during these celebratory seasons to an everyday one. The packaging design should be modern and minimalist yet fun too, also taking into consideration that it should not appear to be too childish. It should stand out from the other snacks products like potato chips etc if placed on the same shelf. The colour scheme is not decided yet as we are open to more ideas but colours should be complementary and not more than 2 or 3 hopefully. There should be also be an enthic sense of south east asian features on the design and it should reflects the Chinese, Malay and indian heritage. It need not be too obvious, a subtle kind should suffice. The packaging should also have the particular graphic/shape of the mould that i have upload followed by the picture of the snack. I have included a mock up of the logo of my company. Proposed designs can feel free to alter the lanternox graphic to a more modern, minimalist yet whimsical and fun. Proposed designs should have a front and back view of the packaging. We are looking to launch at 4 to 5 flavours like white sesame, black sesame, peanuts with white sesame and original.
Updates

Project Deadline Extended
Reason: Not enough submissions coming in yet.

Project Deadline Extended
Reason: Extension of deadline to allow more designs to come in.

Target Market(s)

All ages from as young as 5 to 6 years old to 60 to 70s.

Industry/Entity Type

It Company

Font styles to use
Other font styles liked:
• Fonts should be simple and minimalist. Easy for elderly to read without straining the eyes.

Requirements
Must have
• My logo which I have designed. Designers can feel free to tweak and enhance the design of the logo. The colour is not definite yet. Consumers must know what
• we are selling from the design of the packaging without guessing how it look
• like. The suggested packaging dimension is 17cm (W) by 23.5cm (H).
Nice to have
• We are looking to print the package using kraft paper which I have attached.
Should not have
• religious inclination of motifs, logo etc.

```html
<!DOCTYPE html>
<html lang="en">
<head>
<meta charset="utf-8">
<title>lanternox munchies – black sesame pouch, front and back</title>
<link rel="stylesheet" href="https://fonts.googleapis.com/css2?family=Open+Sans:wght@400;600&family=Arvo:wght@400;700&family=Lora:ital@1&family=Ma+Shan+Zheng&display=swap">
<style>
  :root {
    --backdrop: #5a5a5a;
    --kraft: #d9bb95;
    --kraft-edge: #c9a87f;
    --magenta: #9b1b5f;
    --magenta-faint: rgba(190, 70, 110, 0.45);
    --ink-light: #ffffff;
    --ink-dark: #2b2118;
  }
  * { box-sizing: border-box; margin: 0; padding: 0; }
  html, body { width: 1200px; height: 1000px; overflow: hidden; }
  body { background: var(--backdrop); position: relative; font-family: "Open Sans", Arial, sans-serif; }

  .pouch {
    position: absolute; top: 200px; width: 400px; height: 590px;
    background: var(--kraft); border-radius: 18px 18px 26px 26px;
  }
  .pouch::before {
    content: ""; position: absolute; left: 0; right: 0; top: 40px;
    border-top: 1px solid var(--kraft-edge);
  }
  .pouch--front { left: 190px; }
  .pouch--back { left: 640px; }

  .brand-mark {
    position: absolute; left: 50%; top: 100px; transform: translateX(-50%);
    display: flex; flex-direction: column; align-items: center; gap: 3px;
    color: var(--magenta); font-size: 12px; font-weight: 600;
  }
  .brand-mark .dot { width: 34px; height: 34px; border-radius: 50%; border: 3px solid var(--magenta); }

  .front-label {
    position: absolute; left: 80px; top: 155px; width: 260px; height: 115px;
    background: var(--magenta); color: var(--ink-light);
    border: 2px solid rgba(255,255,255,0.6);
    display: flex; flex-direction: column; align-items: center; justify-content: center; gap: 8px;
  }
  .front-label .product-name { font-size: 21px; }
  .front-label .flavour { font-size: 15px; }

  .chinese-title {
    position: absolute; left: 80px; top: 300px; width: 250px; height: 230px;
    background: var(--magenta-faint); opacity: 0.55; border-radius: 6px;
  }
  .net-weight { position: absolute; left: 0; right: 0; bottom: 28px; text-align: center; font-size: 12px; color: var(--ink-dark); }

  .back-band {
    position: absolute; left: 112px; top: 6px; width: 182px; height: 570px;
    background: var(--magenta); color: var(--ink-light);
    padding: 14px 10px 0; display: flex; flex-direction: column; align-items: center;
  }
  .back-band .dot { width: 44px; height: 44px; border-radius: 50%; border: 3px solid var(--ink-light); }
  .back-band .band-name { font-size: 16px; margin: 8px 0 6px; }

  .nutrition {
    width: 100%; border: 1px solid var(--ink-light); padding: 3px 4px;
    font-family: "Arvo", Georgia, serif; font-size: 5.5px; line-height: 1.35;
  }
  .nutrition h2 { font-size: 10px; border-bottom: 2px solid var(--ink-light); margin-bottom: 2px; }
  .nutrition .big { font-size: 6.5px; font-weight: 700; }
  .nutrition .row { display: flex; justify-content: space-between; }
  .nutrition .rule { border-top: 1px solid var(--ink-light); margin: 2px 0; }
  .nutrition .grid { display: grid; grid-template-columns: 1fr 1fr; }
  .nutrition .tiny { font-size: 4px; }
  .nutrition table { width: 100%; font-size: 4px; border-collapse: collapse; }

  .story { font-family: "Lora", Georgia, serif; font-style: italic; font-size: 8.5px; line-height: 1.35; text-align: center; margin-top: 10px; }
  .story-zh { font-family: "Ma Shan Zheng", serif; font-size: 9px; line-height: 1.3; text-align: center; margin-top: 8px; }
  .contact { font-family: "Arvo", Georgia, serif; font-weight: 700; font-size: 6.5px; line-height: 1.3; text-align: center; margin-top: 10px; border-top: 1px solid var(--ink-light); padding-top: 6px; width: 100%; }
  .band-weight { font-size: 9px; margin-top: auto; margin-bottom: 8px; }
</style>
</head>
<body>

<section class="pouch pouch--front" aria-label="Front of pouch">
  <div class="brand-mark"><span class="dot"></span>lanternox</div>
  <div class="front-label">
    <p class="product-name">lanternox munchies</p>
    <p class="flavour">black sesame</p>
  </div>
  <div class="chinese-title" role="img" aria-label="Large faint brush-lettered Chinese product name"></div>
  <p class="net-weight">Net Weight 70grams</p>
</section>

<section class="pouch pouch--back" aria-label="Back of pouch">
  <div class="back-band">
    <span class="dot"></span>
    <p class="band-name">lanternox munchies</p>

    <div class="nutrition">
      <h2>Nutritional Facts</h2>
      <p>Serving Size 1 Package<br>Serving Per Container 1</p>
      <div class="rule"></div>
      <p class="tiny">Amount Per Serving</p>
      <p class="big">Calories 210<br>Calories from Fat 110</p>
      <p class="tiny" style="text-align:right">% daily value</p>
      <div class="rule"></div>
      <div class="row big"><span>Total Fat 13g</span></div>
      <div class="row"><span>Saturated Fat 2g</span><span>19%</span></div>
      <div class="row"><span>Trans Fat 0g</span><span>9%</span></div>
      <div class="row"><span><b>Cholesterol</b> 0 mg</span><span>0%</span></div>
      <div class="row"><span><b>Sodium</b> 0 mg</span><span>0%</span></div>
      <div class="row"><span><b>Potassium</b> 500mg</span><span>14%</span></div>
      <div class="row"><span><b>Total Carbohydrates</b> 22 g</span><span>7%</span></div>
      <div class="row"><span>Dietary Fibre 2g</span></div>
      <div class="row"><span>Sugars 1g</span></div>
      <div class="row big"><span>Protein 3g</span></div>
      <div class="rule"></div>
      <div class="grid">
        <span>Vitamin A 0%</span><span>Vitamin C 15%</span>
        <span>Calcium 0%</span><span>Vitamin B6 15%</span>
        <span>Iron 4%</span><span>Phosphorus 4%</span>
        <span>Magnesium 6%</span><span>Zinc 2%</span>
      </div>
      <div class="rule"></div>
      <p class="tiny">*Percent Daily Values are based on a 2000 calorie diet. Your daily values may be higher or lower depending on your calorie needs:</p>
      <table>
        <tr><td>Total Fat</td><td>Less than</td><td>65g</td><td>80g</td></tr>
        <tr><td>Sat. Fat</td><td>Less than</td><td>20g</td><td>25g</td></tr>
        <tr><td>Cholesterol</td><td>Less than</td><td>300mg</td><td>300mg</td></tr>
        <tr><td>Sodium</td><td>Less than</td><td>2400mg</td><td>2400mg</td></tr>
        <tr><td>Total Carbohydrate</td><td></td><td>300g</td><td>375g</td></tr>
      </table>
      <div class="rule"></div>
      <p class="big">Ingredients:</p>
      <p class="tiny">Flour, Eggs, Rice Sugar, Coconut milk, Vegetable Oils (Sunflower, Corn and/or Canola Oil)</p>
      <p class="big">Manufactured By :<br>XXXXXXXXXXXXX<br>XXXXXXXXXXXXX</p>
    </div>

    <p class="story">All our munchies are hand fry to perfection. Each one made with love, care and also that traditional flavour you are familiar with.</p>
    <p class="story-zh">每一个脆片都是用手精心的烘焙。每一片都充满了温馨和你熟悉的味道。</p>
    <div class="contact">
      <p>if interested in distributing<br>please call:<br>61234567/69876543</p>
      <p style="margin-top:4px">Like us @<br>www.social.example/lanternox<br>or<br>Visit us @<br>www.lanternoxsnacks.example</p>
    </div>
    <p class="band-weight">Net Weight 70grams</p>
  </div>
</section>

</body>
</html>
```